Coming Soon HTML5 Animated landing page

We need a landing page showing vape movement and our logo (With some discreet movement) stating "Fire Prices on Premium E-Juices Vaping soon" with a contemporary countdown with the colors of our logo. A Countdown will be nice (A contemporary one, Bold) providing all required files. Java Script, CSS, Graphics, Videos and of course HTML....

Target Market(s)

Male/Female 21 - 40 Years Old, Vape Lovers and E-Cigarrette consumers

Coding

Coded - Design and coding required

Number of Pages Required

2 page

Font styles to use
Sans Serif
Other font styles liked:
• Look at our logo

Colors
f37122
ffc214

Requirements
Must have
• A cool HTML5 animation, Vapor movement or exhaled. A configurable count down.
Nice to have
• Would love to see our logo forming
Should not have
• Corny and old concepts...

```html
<!DOCTYPE html>
<html lang="en">
<head>
<meta charset="utf-8">
<title>Quillbrook — Coming Soon</title>
<link rel="stylesheet" href="https://fonts.googleapis.com/css2?family=Open+Sans:wdth,wght@75..100,300..800&display=swap">
<style>
  :root {
    --bg: #0d0d0d;
    --photo-light: #3a3a3a;
    --photo-mid: #262626;
    --photo-dark: #111111;
    --text: #e6e6e6;
    --muted: #9a9a9a;
    --rule: #6a6a6a;
    --accent: #ffc214;
  }
  * { box-sizing: border-box; margin: 0; padding: 0; }
  html, body {
    width: 1200px; height: 789px; overflow: hidden;
    background: var(--bg);
    font-family: "Open Sans", Arial, sans-serif;
    color: var(--text);
  }
  .landing {
    position: relative; width: 1200px; height: 789px; overflow: hidden;
    background: var(--bg);
  }
  .hero-photo {
    position: absolute; inset: 0;
    background:
      radial-gradient(ellipse 420px 520px at 760px 330px, var(--photo-light) 0%, var(--photo-mid) 45%, transparent 80%),
      linear-gradient(90deg, var(--photo-dark) 0%, var(--photo-mid) 55%, var(--photo-dark) 100%);
    opacity: .9;
  }
  .share-toggle {
    position: absolute; left: 20px; top: 132px;
    width: 24px; height: 24px; background: #2a2a2a;
    display: flex; align-items: center; justify-content: center;
  }
  .intro {
    position: absolute; left: 112px; top: 196px;
    font-stretch: 75%; font-weight: 300; text-transform: uppercase;
  }
  .intro__title, .intro__tagline { font-size: 32px; line-height: 1.15; font-weight: 300; white-space: nowrap; }
  .intro__brand { color: var(--accent); }
  .countdown { display: flex; align-items: flex-start; margin-top: 22px; }
  .countdown__unit { text-align: center; padding: 0 26px; border-left: 1px solid var(--rule); }
  .countdown__unit:first-child { border-left: 0; padding-left: 0; }
  .countdown__value { display: block; font-size: 36px; font-weight: 700; line-height: 1; color: #fff; font-stretch: 75%; }
  .countdown__label { display: block; margin-top: 10px; font-size: 9px; color: var(--muted); letter-spacing: .5px; font-stretch: 100%; }
  .notify { margin-top: 30px; }
  .notify__label { font-size: 11px; color: var(--text); font-stretch: 75%; }
  .notify__form {
    margin-top: 22px; width: 200px; display: flex; justify-content: space-between;
    border-bottom: 1px solid var(--rule); padding-bottom: 6px;
    font-size: 11px; text-transform: none; font-stretch: 75%;
  }
  .notify__send { color: var(--text); border-right: 1px solid var(--rule); padding-right: 4px; }
  .next-slide {
    position: absolute; right: 40px; top: 396px;
    width: 30px; height: 30px; border-radius: 50%; background: var(--accent);
    display: flex; align-items: center; justify-content: center;
  }
</style>
</head>
<body>
<main class="landing">
  <div class="hero-photo" role="img" aria-label="Moody black and white portrait photograph with drifting vapour"></div>

  <div class="share-toggle" aria-label="Share">
    <svg width="12" height="12" viewBox="0 0 12 12" fill="none" stroke="#cfcfcf" stroke-width="1.2">
      <circle cx="9" cy="2.5" r="1.6"/><circle cx="2.5" cy="6" r="1.6"/><circle cx="9" cy="9.5" r="1.6"/>
      <path d="M4 5.2 7.5 3.3M4 6.8 7.5 8.7"/>
    </svg>
  </div>

  <section class="intro">
    <h1 class="intro__title"><span class="intro__brand">Quillbrook.com</span> Founded in 2017</h1>
    <p class="intro__tagline">Fire prices on premium e-juices coming soon</p>

    <div class="countdown">
      <div class="countdown__unit"><span class="countdown__value">490</span><span class="countdown__label">DAYS</span></div>
      <div class="countdown__unit"><span class="countdown__value">08</span><span class="countdown__label">HOURS</span></div>
      <div class="countdown__unit"><span class="countdown__value">58</span><span class="countdown__label">MINUTES</span></div>
      <div class="countdown__unit"><span class="countdown__value">24</span><span class="countdown__label">SECONDS</span></div>
    </div>

    <div class="notify">
      <p class="notify__label">Notify me when it's ready</p>
      <div class="notify__form"><span>Email</span><span class="notify__send">Send</span></div>
    </div>
  </section>

  <div class="next-slide" aria-label="Next">
    <svg width="10" height="12" viewBox="0 0 10 12" fill="none" stroke="#fff" stroke-width="1.8">
      <path d="M3 1.5 7.5 6 3 10.5"/>
    </svg>
  </div>
</main>
</body>
</html>
```